Brightmark Pixel Collective Website

I need my website redesigned to look very modern with the latest services. Check out my old website for information: www.brightmarkpixelcollective.com

You can use the same site menu links

It doesn't need to have the Recent News section

Please use the yellow, black and grey color scheme

Target Market(s)

25-50 years in range. Small Business Owners

Industry/Entity Type

Group

Requirements
Must have
• Logo and similar color scheme to current website
• Modern, Modern, Modern! I want a very fresh and modern look
Should not have
• Boring Look

```html
<!DOCTYPE html>
<html lang="en">
<head>
<meta charset="utf-8">
<title>Brightmark Pixel Collective</title>
<link href="https://fonts.googleapis.com/css2?family=Oswald:wght@400;500;700&family=Open+Sans:wght@400;600;700&display=swap" rel="stylesheet">
<style>
:root{
  --yellow:#f8b92e;
  --yellow-deep:#f3a91a;
  --black:#000;
  --ink:#1a1a1a;
  --grey-dark:#3a3a3a;
  --grey-mid:#7a7a7a;
  --grey-light:#d9d9d9;
  --white:#fff;
  --blue:#0b6fc0;
}
*{margin:0;padding:0;box-sizing:border-box}
html,body{width:790px;height:1200px;overflow:hidden}
body{position:relative;font-family:"Open Sans",Arial,sans-serif;background:var(--white);color:var(--ink)}
.abs{position:absolute}
svg{flex:none}

/* header */
.site-header{left:0;top:0;width:790px;height:100px;background:linear-gradient(#fafafa,#d8d8d8);border-top:5px solid #111}
.brand{left:100px;top:56px;display:flex;align-items:center;gap:6px;font-family:"Oswald",sans-serif;font-weight:400;font-size:14px;color:var(--grey-dark);letter-spacing:.2px;white-space:nowrap}
.brand .mark{width:10px;height:10px;background:var(--yellow);flex:none}
.phones{left:438px;top:22px;font-family:"Oswald",sans-serif;font-size:15px;color:#555;white-space:nowrap}
.phones b{color:#222;font-weight:500}
.phones span{margin-left:16px}
.main-nav{left:284px;top:58px;width:506px;height:29px;background:linear-gradient(#2a2a2a,#000);display:flex;align-items:center}
.main-nav .home{width:46px;height:29px;background:var(--yellow);display:flex;align-items:center;justify-content:center;clip-path:polygon(14% 0,100% 0,100% 100%,0 100%)}
.main-nav a{color:var(--white);text-decoration:none;font-size:9px;font-weight:600;padding:0 10px;height:29px;line-height:29px;border-right:1px solid #333;white-space:nowrap}
.main-nav a:last-child{border:none}

/* hero */
.hero{left:0;top:86px;width:790px;height:266px;background:radial-gradient(ellipse at 50% 40%,#fff,#e6e6e6)}
.hero-art{left:108px;top:34px;width:300px;height:192px;border-radius:6px;background:radial-gradient(circle at 50% 55%,#f6b23a 0,#fbe0a0 22%,#e8e8e8 45%,#cfcfcf 100%)}
.hero-title{left:444px;top:40px;font-family:"Oswald",sans-serif;font-weight:700;color:var(--blue);line-height:1}
.hero-title .l1{font-size:74px;letter-spacing:-1px;display:block}
.hero-title .l2{font-size:54px;letter-spacing:-.5px;display:block;margin-top:6px}
.tagline{left:448px;top:186px;width:222px;height:17px;background:#e3e3e3;font-size:9px;letter-spacing:2.2px;line-height:17px;padding-left:8px;color:#222;white-space:nowrap}
.dots{left:378px;top:238px;display:flex;gap:3px}
.dots i{width:9px;height:9px;border-radius:50%;border:1px solid #bbb;background:#fff}
.dots i.on{background:var(--yellow);border-color:#c88a00}

/* services */
.services{left:0;top:352px;width:790px;height:258px;background:linear-gradient(var(--yellow-deep),var(--yellow) 12%)}
.service{top:0;width:150px;height:258px;text-align:center}
.service .icon{width:77px;height:77px;border-radius:50%;background:var(--grey-dark);margin:28px auto 0;display:flex;align-items:center;justify-content:center}
.service .icon.active{background:var(--black);box-shadow:0 0 0 2px var(--black),0 0 0 3px var(--yellow)}
.service h3{font-family:"Oswald",sans-serif;font-weight:500;font-size:16px;line-height:22px;margin-top:12px;color:var(--black);letter-spacing:-.3px;white-space:nowrap}
.service p{font-size:8.8px;line-height:12px;color:#222;margin-top:2px;padding:0 3px;height:62px}
.btn{display:inline-block;font-size:8.5px;font-weight:700;padding:0 6px;height:20px;line-height:20px;text-decoration:none}
.btn-dark{background:var(--black);color:var(--white)}
.btn-yellow{background:var(--yellow);color:var(--black)}
.service .btn{margin-top:10px}
.col-rule{top:25px;width:0;height:210px;border-left:1px dashed rgba(0,0,0,.15)}

/* about */
.about{left:0;top:610px;width:790px;height:472px;background:var(--black);color:var(--white)}
.welcome-panel{left:102px;top:24px;width:251px;height:126px;background:var(--white);display:flex;align-items:center;justify-content:center;gap:8px;font-family:"Oswald",sans-serif;font-size:17px;color:var(--grey-dark);white-space:nowrap}
.welcome-panel .mark{width:13px;height:13px;background:var(--yellow)}
.welcome-title{left:378px;top:20px;width:310px;font-family:"Oswald",sans-serif;font-weight:700;font-size:17.5px;letter-spacing:-.3px;white-space:nowrap}
.welcome-text{left:378px;top:52px;width:308px;font-size:8.3px;line-height:12.6px;color:#ddd;letter-spacing:.15px}
.divider{left:102px;top:170px;width:584px;height:1px;background:linear-gradient(90deg,transparent,#444,transparent)}
.articles-art{left:102px;top:194px;width:251px;height:126px;border:3px solid #bbb;background:radial-gradient(circle at 55% 50%,#1f5fcf 0,#0b2f7a 35%,#05122e 65%,#000 100%)}
.articles-title{left:102px;top:326px;font-family:"Oswald",sans-serif;font-weight:500;font-size:23px;line-height:24px;letter-spacing:-.2px}
.list{list-style:none;font-size:8.4px;color:#eee}
.list li{height:15.3px;padding-left:12px;position:relative;white-space:nowrap}
.list li::before{content:"→";position:absolute;left:0;top:-1px;color:var(--yellow);font-size:8px}
.articles-list{left:102px;top:380px}
.vrule{left:376px;top:192px;width:1px;height:270px;background:#2a2a2a}
.feature{width:140px}
.feature h4{font-family:"Oswald",sans-serif;font-weight:500;font-size:15.5px;display:flex;align-items:center;gap:6px;letter-spacing:-.3px;white-space:nowrap}
.feature p{font-size:8.2px;line-height:10.8px;color:#eee;margin-top:12px;height:54px}
.feature .list{margin-top:12px;height:54px}
.feature .btn{margin-top:6px}

/* footer */
.site-footer{left:0;top:1082px;width:790px;height:118px;background:var(--grey-dark);border-top:3px solid var(--yellow);color:#ddd}
.foot-brand{left:108px;top:26px;display:flex;align-items:center;gap:5px;font-family:"Oswald",sans-serif;font-size:11.5px;color:#cfcfcf;white-space:nowrap}
.foot-brand .mark{width:8px;height:8px;background:var(--yellow)}
.foot-copy{left:122px;top:78px;font-size:7px;color:#ccc}
.follow{left:119px;top:94px;font-size:9.5px;display:flex;align-items:center;gap:3px;color:#ddd}
.follow i{width:10px;height:10px;border-radius:50%;background:#eee;display:inline-block}
.foot-col h5{font-size:10.5px;font-weight:600;color:#eee;padding-bottom:4px;border-bottom:1px dotted #666;width:93px}
.foot-links{list-style:none;font-size:7.6px;margin-top:6px}
.foot-links li{height:15.6px;white-space:nowrap}
.foot-links li::before{content:"› ";color:#aaa}
.contact-line{display:flex;gap:6px;font-size:7.4px;line-height:11px;margin-top:7px;white-space:nowrap}
.inquiry input,.inquiry textarea{display:block;width:122px;height:14px;border:none;background:#f3f3f3;font-size:7px;padding:0 5px;margin-top:4px;font-family:inherit;color:#777}
.inquiry textarea{height:24px;padding-top:3px;resize:none}
.submit{left:632px;top:91px;background:var(--yellow);color:#000;font-size:8px;font-weight:700;padding:2px 7px;border:none}
</style>
</head>
<body>

<header class="site-header abs">
  <div class="brand abs"><span class="mark"></span>Brightmark Pixel Collective</div>
  <div class="phones abs"><b>TOLL FREE :</b> 1-800-555-0142<span><b>Local :</b> 555-204-0188</span></div>
</header>
<nav class="main-nav abs">
  <span class="home"><svg width="16" height="14" viewBox="0 0 16 14"><path d="M8 1 1 7h2v6h4V9h2v4h4V7h2z" fill="#111"/></svg></span>
  <a href="#">WEB DESIGN</a><a href="#">SEARCH ENGINE MARKETING</a><a href="#">SOCIAL MEDIA</a><a href="#">CONTACT US</a>
</nav>

<section class="hero abs">
  <div class="hero-art abs" role="img" aria-label="Three glasses of water with paintbrushes, the centre one glowing orange"></div>
  <h1 class="hero-title abs"><span class="l1">WEB</span><span class="l2">DESIGNING</span></h1>
  <div class="tagline abs">STAND OUT FROM THE CROWD!</div>
  <div class="dots abs"><i></i><i></i><i class="on"></i></div>
</section>

<section class="services abs">
  <div class="service abs" style="left:91px">
    <div class="icon active"><svg width="44" height="44" viewBox="0 0 44 44" fill="none" stroke="#fff" stroke-width="3.5"><circle cx="18" cy="18" r="12"/><circle cx="18" cy="16" r="4" stroke-width="2.5"/><path d="M27 27l10 10" stroke-linecap="round" stroke-width="5"/></svg></div>
    <h3>SARCH ENGINE MARKET</h3>
    <p>When a person goes online to search for a specific product or service they are typically in the buying phase...<br>If you are not AT THE TOP</p>
    <a class="btn btn-dark" href="#">MORE</a>
  </div>
  <div class="col-rule abs" style="left:243px"></div>
  <div class="service abs" style="left:245px">
    <div class="icon"><svg width="44" height="40" viewBox="0 0 44 40" fill="none" stroke="#fff" stroke-width="3"><rect x="3" y="5" width="38" height="24" rx="2"/><path d="M16 36h12M22 29v7"/><path d="M17 24l14-14" stroke-width="3.5"/></svg></div>
    <h3>WEB DESIGN</h3>
    <p>Welcome to Brightmark Pixel Collective. We are very excited and proud to help you achieve the internet solution that you need. We have an experienced.</p>
    <a class="btn btn-dark" href="#">MORE</a>
  </div>
  <div class="col-rule abs" style="left:394px"></div>
  <div class="service abs" style="left:395px">
    <div class="icon"><svg width="52" height="50" viewBox="0 0 52 50" fill="none" stroke="#fff" stroke-width="2"><circle cx="26" cy="25" r="8"/><circle cx="26" cy="7" r="5"/><circle cx="26" cy="43" r="5"/><circle cx="9" cy="16" r="5"/><circle cx="43" cy="16" r="5"/><circle cx="9" cy="34" r="5"/><circle cx="43" cy="34" r="5"/></svg></div>
    <h3>SOCIAL MEDIA</h3>
    <p>Social Networking is the fastest growing and most cost effective marketing platform today. If you don't already understand the #1 reason why your business</p>
    <a class="btn btn-dark" href="#">MORE</a>
  </div>
  <div class="col-rule abs" style="left:545px"></div>
  <div class="service abs" style="left:547px">
    <div class="icon"><svg width="46" height="42" viewBox="0 0 46 42" fill="none" stroke="#fff" stroke-width="3"><rect x="5" y="8" width="32" height="28" rx="2"/><path d="M20 28l18-20 4 4-18 20-6 2z"/></svg></div>
    <h3>GRAPHIC DESIGN</h3>
    <p>You've invested countless hours and a large sum of money to build your online presence, why waste the investment by not marketing it?</p>
    <a class="btn btn-dark" href="#">MORE</a>
  </div>
</section>

<section class="about abs">
  <div class="welcome-panel abs"><span class="mark"></span>Brightmark Pixel Collective</div>
  <h2 class="welcome-title abs">WELCOME TO BRIGHTMARK PIXEL COLLECTIVE</h2>
  <p class="welcome-text abs">We are an award winning web design &amp; internet marketing company located in Minneapolis. As a Minneapolis Web Design company, we create web sites to what our clients want and that's found in our marketing. Here at Brightmark Pixel Collective, we not only design you a first class web presence but market your website so your buyer finds you first before anyone else. A great web presence is built from a client's ideas and the innovative imagination of our Minneapolis Web Designer base and the skills of our internet marketing team.</p>
  <div class="divider abs"></div>

  <div class="articles-art abs" role="img" aria-label="Blue glowing 'web design' lettering over a dark hexagon pattern"></div>
  <h2 class="articles-title abs">TOP ARTICLES WEB DESIGN<br>MINNEAPOLIS</h2>
  <ul class="list articles-list abs">
    <li>Converting Social Media Traffic into Sales</li>
    <li>How much does online marketing cost?</li>
    <li>How to develop a website marketing strategy</li>
  </ul>
  <a class="btn btn-yellow abs" href="#" style="left:102px;top:427px">MORE</a>
  <div class="vrule abs"></div>

  <div class="feature abs" style="left:400px;top:194px">
    <h4><svg width="18" height="18" viewBox="0 0 18 18" fill="none" stroke="#f8b92e" stroke-width="2"><circle cx="9" cy="9" r="7"/><circle cx="9" cy="9" r="3"/><path d="M9 9l8-8"/></svg>OUR MISSION</h4>
    <p>We are an award winning web design &amp; internet marketing company located in Minneapolis Web Design company.</p>
    <a class="btn btn-yellow" href="#">MORE</a>
  </div>
  <div class="feature abs" style="left:547px;top:194px">
    <h4><svg width="18" height="16" viewBox="0 0 18 16"><rect x="0" y="3" width="18" height="13" fill="#f8b92e"/><rect x="6" y="0" width="6" height="4" fill="none" stroke="#f8b92e" stroke-width="2"/></svg>INTERNET MARKETING</h4>
    <p>You've invested countless hours and a large sum of money to build your online presence, why waste the investment by not marketing it?</p>
    <a class="btn btn-yellow" href="#">MORE</a>
  </div>
  <div class="feature abs" style="left:400px;top:334px">
    <h4><svg width="18" height="15" viewBox="0 0 18 15"><path d="M0 2h7l2 2h9v11H0z" fill="#f8b92e"/></svg>DEVELOPMENT</h4>
    <ul class="list"><li>Lorem ipsum dolor sit amet</li><li>Lorem ipsum dolor sit amet</li><li>Lorem ipsum dolor sit amet</li></ul>
    <a class="btn btn-yellow" href="#">MORE</a>
  </div>
  <div class="feature abs" style="left:547px;top:334px">
    <h4><svg width="18" height="16" viewBox="0 0 18 16" fill="none" stroke="#f8b92e" stroke-width="2"><rect x="1" y="3" width="14" height="10"/><path d="M7 10l9-9"/></svg>WEBDESIGN</h4>
    <p>Welcome to Brightmark Pixel Collective. We are very excited and proud to help you achieve the internet solution that you need.</p>
    <a class="btn btn-yellow" href="#">MORE</a>
  </div>
</section>

<footer class="site-footer abs">
  <div class="foot-brand abs"><span class="mark"></span>Brightmark Pixel Collective</div>
  <div class="foot-copy abs">@ 2014 | PRIVACY POLICY</div>
  <div class="follow abs">Follow Us : <i></i><i></i><i></i></div>

  <div class="foot-col abs" style="left:258px;top:11px">
    <h5>Quick Links</h5>
    <ul class="foot-links"><li>Home</li><li>Web Design</li><li>Search Engine Marketing</li><li>Social Media</li><li>Contact Us</li></ul>
  </div>
  <div class="foot-col abs" style="left:397px;top:11px">
    <h5>Contact Details</h5>
    <div class="contact-line"><svg width="8" height="11" viewBox="0 0 8 11"><path d="M4 0a4 4 0 0 1 4 4c0 3-4 7-4 7S0 7 0 4a4 4 0 0 1 4-4z" fill="#aaa"/><circle cx="4" cy="4" r="1.5" fill="#3a3a3a"/></svg><span>Lorem ipsum dolor sit amet<br>consectetuer adipiscing elit<br>sed diam nonummy.</span></div>
    <div class="contact-line"><svg width="9" height="9" viewBox="0 0 9 9"><path d="M1 1l2-1 1.5 2.5-1 1a5 5 0 0 0 2 2l1-1L9 6 8 8C4 8 1 5 1 1z" fill="#aaa"/></svg><span>123-456-7890</span></div>
    <div class="contact-line"><svg width="10" height="8" viewBox="0 0 10 8"><rect width="10" height="8" fill="#aaa"/><path d="M0 0l5 4 5-4" stroke="#3a3a3a" fill="none"/></svg><span>info@brightmarkpixelcollective.com</span></div>
  </div>
  <div class="foot-col inquiry abs" style="left:552px;top:11px">
    <h5 style="border:none">Quick Inquiry</h5>
    <input type="text" placeholder="Name"><input type="text" placeholder="Email"><textarea placeholder="Message"></textarea>
  </div>
  <button class="submit abs">SUBMIT</button>
</footer>

</body>
</html>
```